Unique business card design

Boutique coastal hotel suites - in need of clever stand out business card I have uploaded the logo that I had created through quill forge I want something that is clever and stands out from everyone else - 418 Brantwell Avenue halvik Alaska 99571 phone or text 907 -581-6142 www.primemarrowbysuites.com

Target Market(s)

Men and woman

Industry/Entity Type

Boutique coastal hotel

Contact Information for Business Card

Marrowby Suites halvik Alaska marrowby_suites@mailnest.net

Requirements
Must have
• Classy - clever -bold 907-581-6142 call or text

```html
<!DOCTYPE html>
<html lang="en">
<head>
<meta charset="utf-8">
<title>Marrowby Suites — Business Card</title>
<link rel="stylesheet" href="https://fonts.googleapis.com/css2?family=Montserrat:wght@400;500;700;800&display=swap">
<style>
  :root {
    --navy: #344f6c;
    --navy-light: #55708d;
    --white: #ffffff;
    --ink: #2b2b2b;
    --backdrop: #1f1f1f;
  }
  * { margin: 0; padding: 0; box-sizing: border-box; }
  html, body { width: 1200px; height: 988px; overflow: hidden; }
  body {
    background: var(--backdrop);
    font-family: "Montserrat", Arial, sans-serif;
    position: relative;
  }
  .card {
    position: absolute;
    left: 232px;
    width: 735px;
    height: 420px;
    border-radius: 22px;
    overflow: hidden;
  }
  .card-back {
    top: 49px;
    background: linear-gradient(135deg, var(--navy-light) 0%, var(--navy) 55%);
  }
  .card-front {
    top: 518px;
    background: var(--white);
  }
  .wordmark {
    position: absolute;
    display: flex;
    align-items: center;
    gap: 16px;
    font-weight: 700;
    letter-spacing: 0.06em;
    text-transform: uppercase;
    white-space: nowrap;
  }
  .wordmark-square {
    width: 26px;
    height: 26px;
    background: currentColor;
    flex: none;
  }
  .card-back .wordmark {
    left: 50%;
    top: 50%;
    transform: translate(-50%, -50%);
    color: var(--white);
    font-size: 54px;
  }
  .card-front .wordmark {
    left: 50%;
    top: 60px;
    transform: translateX(-50%);
    color: var(--navy);
    font-size: 40px;
  }
  .wordmark-rule {
    position: absolute;
    height: 3px;
  }
  .card-back .wordmark-rule { left: 160px; right: 160px; top: 262px; background: var(--white); }
  .card-front .wordmark-rule { left: 200px; right: 200px; top: 122px; background: var(--navy); }
  .person {
    position: absolute;
    left: 24px;
    top: 192px;
    width: 330px;
    text-align: right;
    white-space: nowrap;
  }
  .person-name {
    color: var(--navy);
    font-size: 30px;
    font-weight: 800;
    letter-spacing: 0.02em;
    line-height: 1.1;
  }
  .person-role {
    color: var(--ink);
    font-size: 16px;
    margin-top: 4px;
  }
  .divider {
    position: absolute;
    left: 378px;
    top: 168px;
    width: 2px;
    height: 94px;
    background: var(--navy);
  }
  .contacts {
    position: absolute;
    left: 404px;
    top: 170px;
    list-style: none;
    white-space: nowrap;
  }
  .contacts li {
    display: flex;
    align-items: center;
    gap: 10px;
    font-size: 14px;
    color: var(--ink);
    height: 30px;
  }
  .contacts svg { width: 16px; height: 16px; flex: none; }
  .address-band {
    position: absolute;
    left: 0;
    right: 0;
    top: 300px;
    height: 56px;
    background: var(--navy);
    color: var(--white);
    display: flex;
    align-items: center;
    justify-content: center;
    font-size: 18px;
    font-weight: 500;
    letter-spacing: 0.02em;
    white-space: nowrap;
  }
</style>
</head>
<body>
  <section class="card card-back" aria-label="Card back">
    <div class="wordmark"><span class="wordmark-square"></span>Marrowby Suites</div>
    <div class="wordmark-rule"></div>
  </section>

  <section class="card card-front" aria-label="Card front">
    <div class="wordmark"><span class="wordmark-square"></span>Marrowby Suites</div>
    <div class="wordmark-rule"></div>

    <div class="person">
      <div class="person-name">DANE CARLOW</div>
      <div class="person-role">Project Manager</div>
    </div>

    <div class="divider"></div>

    <ul class="contacts">
      <li>
        <svg viewBox="0 0 16 16" aria-hidden="true"><path fill="#344f6c" d="M3.5 1.5l2.5 2.8-1.3 1.8c.8 1.9 2.3 3.4 4.2 4.2l1.8-1.3 2.8 2.5-1.6 2.6C6.6 13.6 2.4 9.4 1 3.1z"/></svg>
        907 -581-6142
      </li>
      <li>
        <svg viewBox="0 0 16 16" aria-hidden="true"><rect x="1" y="3" width="14" height="10" rx="1.5" fill="#344f6c"/><path d="M2 4.5l6 4.5 6-4.5" stroke="#fff" stroke-width="1.4" fill="none"/></svg>
        alaskamarrowby_suites@mailnest.net
      </li>
      <li>
        <svg viewBox="0 0 16 16" aria-hidden="true"><circle cx="8" cy="8" r="6.5" fill="none" stroke="#344f6c" stroke-width="1.6"/><path d="M1.5 8h13M8 1.5c2.4 2.5 2.4 10.5 0 13M8 1.5c-2.4 2.5-2.4 10.5 0 13" stroke="#344f6c" stroke-width="1.2" fill="none"/></svg>
        www.primemarrowbysuites.com
      </li>
    </ul>

    <div class="address-band">418 Brantwell Avenue halvik Alaska 99571</div>
  </section>
</body>
</html>
```